Label design for outdoor terrace cleaner

We are Dermik Patio Living and searching for a modern, clean but colorful and exciting label packaging design. Our product is Brightstep Deck and is a weedage and terrace cleaner. It is a consumer product for webshops and retail shops, which should stand out by design and colors. We also would like it to be very visibly appealing with a photo.

Label size: 240 mm x 176 mm

Logo: DERMIK (Please adjust to any color you want)
Slogan: PATIO LIVING (as part of the logo)

Label text is dutch, if you need any help with that, please ask.
Updates

Low design quality

Target Market(s)

Outdoor cleaning, retail market, handy shops, consumer retail market

Industry/Entity Type

Cleaning Product

Colors

Designer to choose colors to be used in the design.

Requirements
Must have
• Original ideas, marketing thoughts, some extra brainstorming for an outstanding and original result including texts, that will have consumers see our product and want to buy it. Smart use of words, photos and colors.
Nice to have
• Bright and visibly appealing colors (should include green, but nothing standard) and photo
Should not have
• Standard, dull appearance

```html
<!DOCTYPE html>
<html lang="nl">
<head>
<meta charset="utf-8">
<title>Dermik Patio Living – Brightstep Deck label</title>
<link rel="stylesheet" href="https://fonts.googleapis.com/css2?family=Anton&family=Poppins:wght@300;400&display=swap">
<style>
  :root {
    --orange: #e2702f;
    --ink: #1d1d1b;
    --panel: rgba(255, 255, 255, 0.42);
    --logo-panel: rgba(255, 255, 255, 0.5);
    --white: #ffffff;
    --page: #ffffff;
  }
  html, body {
    margin: 0;
    padding: 0;
    width: 1131px;
    height: 1200px;
    overflow: hidden;
    background: var(--page);
    font-family: "Poppins", sans-serif;
    color: var(--ink);
  }
  .label {
    position: absolute;
    left: 20px;
    top: 150px;
    width: 1091px;
    height: 800px;
    overflow: hidden;
  }
  .label-photo {
    position: absolute;
    inset: 0;
    background: linear-gradient(180deg,
      #8fbde0 0%, #c9dce6 12%, #efe6cf 26%, #d9d98a 36%,
      #9cc24a 48%, #8fb33c 60%, #c9b48e 70%, #d8c3a2 82%, #cdb08a 100%);
  }
  .bands {
    position: absolute;
    inset: 0;
  }
  .logo-panel {
    position: absolute;
    left: 29px;
    top: 85px;
    width: 491px;
    height: 153px;
    background: var(--logo-panel);
    border-radius: 6px;
    display: flex;
    align-items: center;
    justify-content: center;
  }
  .brand-name {
    font-family: "Anton", sans-serif;
    font-size: 132px;
    line-height: 1;
    letter-spacing: 2px;
    color: var(--orange);
  }
  .brand-tagline {
    position: absolute;
    left: 29px;
    width: 491px;
    top: 252px;
    text-align: center;
    font-family: "Poppins", sans-serif;
    font-weight: 400;
    font-size: 26px;
    letter-spacing: 0.5px;
  }
  .benefits {
    position: absolute;
    left: 142px;
    width: 300px;
    top: 502px;
    margin: 0;
    padding: 0;
    list-style: none;
    text-align: center;
    font-weight: 300;
    font-size: 18px;
    letter-spacing: -0.8px;
  }
  .benefits li { height: 46.5px; line-height: 30px; }
  .footer-claim {
    position: absolute;
    left: 22px;
    top: 742px;
    color: var(--white);
    font-weight: 300;
    font-size: 15px;
    line-height: 19px;
  }
  .info-panel {
    position: absolute;
    background: var(--panel);
    border-radius: 8px;
    font-size: 12.6px;
    font-weight: 300;
    line-height: 29px;
    padding: 4px 18px 0 10px;
    box-sizing: border-box;
  }
  .info-panel h2 {
    margin: 0;
    font-size: 12.6px;
    font-weight: 400;
  }
  .info-panel ul {
    margin: 0;
    padding: 0;
    list-style: none;
    text-align: justify;
  }
  .info-panel li::before { content: "•  "; }
  .use-panel { left: 572px; top: 121px; width: 495px; height: 259px; }
  .notes-panel { left: 577px; top: 442px; width: 490px; height: 262px; }
  .caption {
    position: absolute;
    top: 968px;
    font-family: "Poppins", sans-serif;
    font-size: 26px;
    font-weight: 400;
  }
  .caption-front { left: 245px; }
  .caption-back { left: 790px; }
</style>
</head>
<body>
  <section class="label" aria-label="Brightstep Deck label, front and back">
    <div class="label-photo" role="img" aria-label="Photo of a sunny sky over green hills with a wooden deck in the foreground"></div>

    <svg class="bands" width="1091" height="800" viewBox="0 0 1091 800" aria-hidden="true">
      <path fill="var(--orange)" d="M578 0 C620 40 660 58 720 60 C820 62 900 58 970 70 C1030 82 1070 110 1091 128 L1091 0 Z"/>
      <path fill="var(--orange)" d="M0 640 C60 690 140 730 230 732 C330 732 420 718 480 726 C560 738 600 760 632 800 L0 800 Z"/>
    </svg>

    <div class="logo-panel">
      <span class="brand-name">DERMIK</span>
    </div>
    <div class="brand-tagline">PATIO LIVING</div>

    <ul class="benefits">
      <li>Zonder glyfosfaat</li>
      <li>Concentraat zonder giftige stoffen</li>
      <li>Resultaat binnen enkele uren</li>
      <li>Voor paden en terrassen</li>
    </ul>

    <p class="footer-claim">Groen terras.<br>De must-have reiniger voor alle type terrassen, voor ieder huishouden.</p>

    <div class="info-panel use-panel">
      <h2>Useinstructions:</h2>
      <ul>
        <li>Verdun het tot een 25% oplossing (bijv. 1 liter Brightstep Deck en 3 liter water).</li>
        <li>Besproei of begiet het terras met deze oplossing. 2 liter per 10 m2. (1 liter Brightstep Deck is dus voldoende voor ca. 20 m2 terras).</li>
        <li>Niet toepassen in de volle zon en als er binnen enkele uren veel neerslag wordt verwacht.</li>
        <li>Eventueel na enkele dagen het los gekomen vuil van het terras vegen of spuiten.</li>
      </ul>
    </div>

    <div class="info-panel notes-panel">
      <h2>Notes:</h2>
      <ul>
        <li>Op zeer hardnekkige vervuiling kan het product eventueel onverdund worden toegepast.</li>
        <li>Brightstep Deck tast bij toepassing conform de gebruiksaanwijzing gangbare buiten (natuur)steen, tegels en hout niet aan.</li>
        <li>Voorkom dat reinigingsproducten in contact komen met gewassen en/of direct in het oppervlaktewater terecht komen.</li>
        <li>Neem veiligheidsmaatregel in acht bij het werken met het onverdunde product.</li>
      </ul>
    </div>
  </section>

  <div class="caption caption-front">Front</div>
  <div class="caption caption-back">Back</div>
</body>
</html>
```